Build PowerPoint for New Logo & Letterhead

I have started my own consulting firm and created a logo and letterhead (attached) am looking PowerPoint template. My name is Dorian Pekkarinen and the company is called Q Harbor Consulting. We primarily use PowerPoint files to display analyses, maps and key talking points from interviews and/or recommendations. We use the documents more to facilitate discussion with our target audiences. Most of the time our PowerPoint document is printed as handouts for our clients and not projected.

Target Market(s)

Healthcare provider organizations (hospitals, health systems, physician groups)

Industry/Entity Type

Healthcare

Font styles to use
Sans Serif

Colors
abd036
1f9ad1
0355a3

Requirements
Must have
• I would like to cover page to play off of the letterhead in some fashion. I want the design to provide plenty of space for text, graphics, maps, pictures, etc.
• We will usually include our clients logo somewhere on the document. Historically it is prominent on the cover page and then in one of the corners on all of the pages thereafter.

```html
<!DOCTYPE html>
<html lang="en">
<head>
<meta charset="utf-8">
<title>Q Harbor Consulting – Presentation Template</title>
<link href="https://fonts.googleapis.com/css2?family=Roboto:wght@400;500;700&display=swap" rel="stylesheet">
<style>
  :root {
    --green: #abd036;
    --green-deep: #9cc83a;
    --blue: #1f9ad1;
    --blue-mid: #2a88c9;
    --navy: #0355a3;
    --grey: #6d6e70;
    --ink: #1d1d1d;
    --paper: #f7f7f7;
    --backdrop-top: #5d7886;
    --backdrop-bottom: #33495a;
  }
  * { box-sizing: border-box; margin: 0; padding: 0; }
  html, body { width: 755px; height: 1200px; overflow: hidden; }
  body {
    font-family: "Roboto", Arial, sans-serif;
    background: radial-gradient(ellipse at 50% 45%, var(--backdrop-top), var(--backdrop-bottom));
    position: relative;
  }
  .slide {
    position: absolute; left: 20px; width: 718px; height: 537px;
    background: radial-gradient(ellipse at 50% 40%, #ffffff, #ececec);
    box-shadow: 0 4px 10px rgba(0,0,0,.45);
    overflow: hidden;
  }
  .cover { top: 20px; }
  .content { top: 578px; }

  /* cover */
  .brand { position: absolute; top: 78px; left: 0; width: 100%; text-align: center; }
  .brand-name { font-size: 64px; font-weight: 700; color: var(--blue-mid); letter-spacing: 4px; line-height: 1; }
  .brand-sub { margin-top: 40px; font-size: 24px; font-weight: 500; color: var(--grey); letter-spacing: 9px; }
  .cover-band { position: absolute; left: 0; top: 258px; }
  .cover-title { position: absolute; top: 284px; width: 100%; text-align: center; color: #fff; font-size: 18px; font-weight: 500; }
  .credit { position: absolute; top: 375px; width: 240px; text-align: center; color: #fff; font-size: 14px; }
  .credit.to { left: 90px; } .credit.by { left: 390px; }
  .credit-label { font-weight: 500; margin-bottom: 26px; }
  .credit-name { font-weight: 700; line-height: 18px; }
  .credit-detail { font-weight: 500; line-height: 18px; }
  .contact-bar { position: absolute; left: 0; bottom: 0; width: 100%; height: 44px; background: var(--green-deep); color: #fff; font-size: 12px; }
  .contact { position: absolute; top: 10px; display: flex; align-items: center; gap: 17px; }
  .contact svg { width: 24px; height: 24px; }
  .contact.phone { left: 29px; } .contact.mail { left: 263px; } .contact.web { left: 518px; }

  /* content slide */
  .top-rule { position: absolute; top: 0; left: 0; width: 100%; height: 6px; background: var(--blue); }
  .page-tab { position: absolute; top: 0; right: 0; }
  .page-num { position: absolute; top: 10px; right: 28px; color: #fff; font-size: 26px; font-weight: 500; }
  .mini-mark { position: absolute; top: 21px; left: 14px; width: 26px; height: 26px; background: var(--blue); }
  .title-divider { position: absolute; top: 20px; left: 57px; width: 1px; height: 30px; background: #bbb; }
  .slide-title { position: absolute; top: 22px; left: 73px; color: var(--green-deep); font-size: 23px; font-weight: 500; }
  .body-copy { position: absolute; top: 98px; left: 35px; width: 648px; font-size: 17px; line-height: 22px; color: var(--ink); text-align: justify; text-indent: 26px; }
  .timeline { position: absolute; left: 0; top: 0; }
  .year { position: absolute; top: 353px; font-size: 15px; font-weight: 700; color: var(--ink); }
  .year.start { left: 14px; } .year.end { left: 664px; }
  .milestone { position: absolute; width: 180px; text-align: center; font-size: 12px; line-height: 16px; color: #333; }
  .slide-footer-rule { position: absolute; top: 512px; left: 13px; width: 690px; height: 1px; background: var(--green); }
  .slide-footer { position: absolute; top: 520px; font-size: 10px; color: #222; }
  .slide-footer.left { left: 13px; } .slide-footer.right { right: 14px; }

  .backdrop-brand { position: absolute; top: 1133px; width: 100%; text-align: center; color: #fff; }
  .backdrop-brand .name { font-size: 22px; font-weight: 700; letter-spacing: 2px; line-height: 1; }
  .backdrop-brand .sub { font-size: 8px; letter-spacing: 3px; margin-top: 6px; }
</style>
</head>
<body>

<section class="slide cover">
  <div class="brand">
    <div class="brand-name">Q HARBOR</div>
    <div class="brand-sub">CONSULTING</div>
  </div>
  <svg class="cover-band" width="718" height="279" viewBox="0 0 718 279">
    <defs>
      <linearGradient id="bandFill" x1="0" y1="0" x2="0" y2="1">
        <stop offset="0" stop-color="#2a93d6"/><stop offset="1" stop-color="#2586c6"/>
      </linearGradient>
    </defs>
    <rect x="0" y="50" width="718" height="6" fill="var(--green-deep)"/>
    <path d="M0 56 L60 56 Q80 56 88 30 Q96 4 125 4 L593 4 Q622 4 630 30 Q638 56 658 56 L718 56 L718 235 L0 235 Z" fill="url(#bandFill)"/>
  </svg>
  <div class="cover-title">PRESENTATION TITLE</div>
  <div class="credit to">
    <div class="credit-label">PRESENTED TO</div>
    <div class="credit-name">Company/Client Name</div>
    <div class="credit-detail">27 Oct 2015</div>
  </div>
  <div class="credit by">
    <div class="credit-label">PRESENTED BY</div>
    <div class="credit-name">Dorian Pekkarinen</div>
    <div class="credit-detail">Consultant</div>
  </div>
  <div class="contact-bar">
    <div class="contact phone">
      <svg viewBox="0 0 24 24" fill="none" stroke="#fff" stroke-width="1.2"><circle cx="12" cy="12" r="11"/><rect x="9" y="6.5" width="6" height="11" rx="1"/><line x1="11" y1="15.5" x2="13" y2="15.5"/></svg>
      <span>555.014.2290</span>
    </div>
    <div class="contact mail">
      <svg viewBox="0 0 24 24" fill="none" stroke="#fff" stroke-width="1.2"><circle cx="12" cy="12" r="11"/><rect x="6.5" y="8" width="11" height="8"/><polyline points="6.5,8 12,12.5 17.5,8"/></svg>
      <span>dorian@qharborconsulting.co</span>
    </div>
    <div class="contact web">
      <svg viewBox="0 0 24 24" fill="none" stroke="#fff" stroke-width="1.2"><circle cx="12" cy="12" r="11"/><circle cx="12" cy="12" r="6"/><ellipse cx="12" cy="12" rx="2.5" ry="6"/><line x1="6" y1="12" x2="18" y2="12"/></svg>
      <span>www.qharborconsulting.co</span>
    </div>
  </div>
</section>

<section class="slide content">
  <div class="top-rule"></div>
  <svg class="page-tab" width="110" height="52" viewBox="0 0 110 52">
    <path d="M0 0 L110 0 L110 52 L40 52 Q24 52 18 32 Q10 6 0 4 Z" fill="var(--blue)"/>
  </svg>
  <div class="page-num">02</div>
  <div class="mini-mark"></div>
  <div class="title-divider"></div>
  <h1 class="slide-title">THIS IS THE SLIDE TITLE</h1>
  <p class="body-copy">Lorem ipsum dolor sit amet, consectetur adipiscing elit. Vestibulum dolor elit, mattis non quam sed, sodales vestibulum justo. Cras sed accumsan mi, in auctor nisi. Aenean mattis justo molestie, hendrerit velit eget, auctor est. Suspendisse mauris mi, pretium eu rhoncus nec, gravida ut lectus. Aliquam faucibus lorem ut rutrum tempor.</p>

  <svg class="timeline" width="718" height="480" viewBox="0 0 718 480">
    <line x1="65" y1="362" x2="655" y2="362" stroke="#888" stroke-width="1.5"/>
    <g stroke-width="2" fill="#fff">
      <circle cx="145" cy="362" r="7" stroke="#8a4cb0"/><circle cx="145" cy="362" r="4" fill="#8a4cb0" stroke="none"/>
      <circle cx="288" cy="362" r="7" stroke="#2f74d6"/><circle cx="288" cy="362" r="4" fill="#2f74d6" stroke="none"/>
      <circle cx="431" cy="362" r="7" stroke="#4f9a48"/><circle cx="431" cy="362" r="4" fill="#4f9a48" stroke="none"/>
      <circle cx="574" cy="362" r="7" stroke="#d14a6e"/><circle cx="574" cy="362" r="4" fill="#d14a6e" stroke="none"/>
    </g>
    <!-- magnifier -->
    <circle cx="138" cy="285" r="25" fill="#8a4cb0" stroke="#8a4cb0" stroke-width="4"/>
    <circle cx="138" cy="285" r="21" fill="none" stroke="#fff" stroke-width="3"/>
    <line x1="156" y1="303" x2="176" y2="325" stroke="#8a4cb0" stroke-width="4" stroke-linecap="round"/>
    <!-- eye -->
    <path d="M254 420 Q288 382 322 420 Q288 458 254 420 Z" fill="#2f74d6"/>
    <circle cx="288" cy="420" r="12" fill="#fff"/><circle cx="288" cy="420" r="7" fill="#2f74d6"/>
    <!-- open envelope -->
    <path d="M400 280 L431 255 L462 280 L462 322 L400 322 Z" fill="#4f9a48"/>
    <rect x="414" y="262" width="34" height="30" fill="#fff"/>
    <g stroke="#4f9a48" stroke-width="2"><line x1="420" y1="270" x2="442" y2="270"/><line x1="420" y1="277" x2="442" y2="277"/><line x1="420" y1="284" x2="436" y2="284"/></g>
    <path d="M400 282 L431 305 L462 282 L462 322 L400 322 Z" fill="#5aa853"/>
    <path d="M400 322 L431 300 L462 322 Z" fill="#4f9a48"/>
    <!-- star -->
    <polygon points="574,398 582,422 608,422 587,437 595,462 574,447 553,462 561,437 540,422 566,422" fill="#d14a6e"/>
  </svg>
  <div class="year start">2006</div>
  <div class="year end">2016</div>
  <div class="milestone" style="left:55px; top:381px;">Lorem ipsum dolor sit amet,<br>consectetur adipiscing elit.</div>
  <div class="milestone" style="left:198px; top:312px;">Vestibulum dolor elit,<br>mattis non quam sed.</div>
  <div class="milestone" style="left:341px; top:381px;">Cras sed accumsan mi,<br>in auctor nisi.</div>
  <div class="milestone" style="left:484px; top:294px;">Aenean mattis justo<br>molestie, hendrerit velit eget,<br>auctor est.</div>

  <div class="slide-footer-rule"></div>
  <div class="slide-footer left">Copyright 2016 Q Harbor Consulting. All rights reserved.</div>
  <div class="slide-footer right">www.qharborconsulting.co</div>
</section>

<div class="backdrop-brand">
  <div class="name">Q HARBOR</div>
  <div class="sub">CONSULTING</div>
</div>

</body>
</html>
```